Project Management - Web Design Project

Vantrel 4 Management Limited is a company which provides specialist Project Control and Contract Management expertise to the Engineering, Construction and Manufacturing industries. The emphasis is on advanced Project Management techniques in particular Planning & Scheduling, Cost Control, Change Control, Risk Management, Reporting and Contract Administration. We are a global company (albeit a small start-up at this time) and pride ourselves on our ability to support projects to help them achieve their goals and objectives. Our aim is to implement work class control tools in a simple and user friendly manner. We would like the website to appear professional but at the same time easy to navigate and a good balance between text and pictures. The final design should communicate our value added service to our customers, our willingness to support and our structured approach to our work.

Target Market(s)

Project Management professionals working for engineering, construction and manufacturing organisations involved with delivering projects.

Industry/Entity Type

Construction

Requirements
Must have
• The website must include all of the content from the attached Excel brief. The company logo (attached) must also be included in the design. The design must portray a professional look and feel. Please include pictures and photographs related to project management in the engineering, construction and manufacturing industries. We may supplement with pictures of our own during the next steps.
Nice to have
• Emphasis that Vantrel 4 is available to support, guide, direct to achieve positive outcomes for the projects. We work hard at developing our customer relationships. Our employees are experienced in advanced project management techniques.
Should not have
• The design should not use old style fonts. It should look modern and professional. Do not include cartoons or silly illustrations.

```html
<!DOCTYPE html>
<html lang="en">
<head>
<meta charset="utf-8">
<title>Vantrel 4 Management Limited</title>
<link rel="stylesheet" href="https://fonts.googleapis.com/css2?family=Marcellus&family=Montserrat:wght@400;500&family=Open+Sans:wght@400;600&display=swap">
<style>
  :root {
    --navy-top: #0b1e4a;
    --navy-deep: #061233;
    --nav-grey-top: #f3f3f3;
    --nav-grey-bottom: #d4d4d4;
    --hero-dark: #041235;
    --hero-mid: #0c3c9a;
    --hero-glow: #1a6ad8;
    --headline-yellow: #f6e477;
    --tick-green: #5fc43a;
    --button-yellow: #f2dc2c;
    --button-yellow-dark: #d8b90e;
    --text-dark: #333333;
    --text-body: #444444;
    --link-blue: #2e8fd8;
    --rule-grey: #c9c9c9;
    --footer-bg: #1b1b1b;
    --footer-text: #e8e8e8;
    --phone-yellow: #f3d21c;
    --white: #ffffff;
  }
  * { box-sizing: border-box; margin: 0; padding: 0; }
  html, body { width: 1200px; height: 594px; overflow: hidden; background: var(--white); }
  body { position: relative; font-family: "Open Sans", Arial, sans-serif; color: var(--text-body); }

  .utility-bar {
    position: absolute; left: 0; top: 0; width: 1200px; height: 30px;
    background: linear-gradient(var(--navy-top), var(--navy-deep));
  }
  .utility-links { position: absolute; right: 200px; top: 0; height: 30px; display: flex; align-items: center; list-style: none; }
  .utility-links li { font-family: "Montserrat", sans-serif; font-size: 12px; color: var(--white); padding: 0 12px; border-left: 1px solid rgba(255,255,255,.25); line-height: 30px; white-space: nowrap; }
  .utility-links li:first-child { border-left: none; }
  .social-dots { position: absolute; left: 1008px; top: 8px; display: flex; gap: 5px; }
  .social-dots span { width: 15px; height: 15px; border-radius: 50%; background: #d8dde8; }

  .main-nav {
    position: absolute; left: 0; top: 30px; width: 1200px; height: 50px;
    background: linear-gradient(var(--nav-grey-top), var(--nav-grey-bottom));
  }
  .brand { position: absolute; left: 140px; top: 10px; display: flex; align-items: center; gap: 8px; }
  .brand-mark { width: 28px; height: 28px; border-radius: 50%; background: var(--navy-top); }
  .brand-name { font-family: "Montserrat", sans-serif; font-weight: 500; font-size: 19px; color: var(--navy-top); }
  .nav-links { position: absolute; right: 136px; top: 0; height: 50px; display: flex; align-items: center; gap: 19px; list-style: none; }
  .nav-links li { font-family: "Montserrat", sans-serif; font-weight: 500; font-size: 14.5px; color: var(--text-dark); white-space: nowrap; }

  .hero {
    position: absolute; left: 0; top: 80px; width: 1200px; height: 266px; z-index: 2;
    background: radial-gradient(ellipse 520px 300px at 760px 140px, var(--hero-glow), var(--hero-mid) 45%, var(--hero-dark) 100%);
  }
  .hero-title { position: absolute; left: 140px; top: 26px; font-family: "Marcellus", serif; font-size: 29px; color: var(--headline-yellow); font-weight: 400; white-space: nowrap; }
  .hero-points { position: absolute; left: 140px; top: 83px; list-style: none; }
  .hero-points li { height: 30px; display: flex; align-items: center; gap: 10px; font-size: 14.5px; color: var(--white); font-weight: 600; white-space: nowrap; }
  .hero-points svg { width: 14px; height: 12px; }
  .cta-button {
    position: absolute; left: 142px; top: 234px; width: 162px; height: 36px;
    background: linear-gradient(#fbef6b, var(--button-yellow) 55%, var(--button-yellow-dark));
    border-radius: 3px; box-shadow: 0 4px 6px rgba(0,0,0,.4);
    font-family: "Marcellus", serif; font-size: 17px; color: #3a3200; display: flex; align-items: center; padding-left: 11px; white-space: nowrap;
  }
  .cta-arrow { position: absolute; right: 8px; top: 9px; width: 18px; height: 18px; background: #4a4a36; border-radius: 2px; display: flex; align-items: center; justify-content: center; }
  .hero-visual {
    position: absolute; left: 580px; top: 0; width: 370px; height: 266px;
    background: radial-gradient(ellipse 160px 190px at 240px 170px, rgba(235,240,250,.55), rgba(40,90,190,0) 70%),
                radial-gradient(ellipse 140px 120px at 90px 90px, rgba(200,220,255,.35), rgba(40,90,190,0) 70%);
  }
  .slider-controls {
    position: absolute; left: 961px; top: 242px; width: 103px; height: 24px;
    background: linear-gradient(#f4f4f4, #cfcfcf); border-radius: 4px 4px 0 0;
    display: flex; align-items: center; justify-content: space-around; padding: 0 10px;
  }

  .hero-base { position: absolute; left: 0; top: 346px; width: 1200px; height: 16px; background: linear-gradient(#d8d8d8, #ffffff); z-index: 1; }

  .service-columns { position: absolute; left: 0; top: 366px; width: 1200px; height: 198px; }
  .service-column { position: absolute; top: 0; height: 198px; }
  .service-column + .service-column::before {
    content: ""; position: absolute; left: -29px; top: 0; width: 1px; height: 190px;
    background: linear-gradient(rgba(0,0,0,.12), rgba(0,0,0,0));
  }
  .service-column h2 { font-family: "Montserrat", sans-serif; font-weight: 400; font-size: 15px; color: var(--link-blue); padding-top: 32px; padding-bottom: 7px; border-bottom: 1px solid var(--rule-grey); white-space: nowrap; }
  .service-column ul { list-style: none; margin-top: 9px; }
  .service-column li { font-size: 12px; color: var(--text-body); height: 24.5px; display: flex; align-items: center; gap: 9px; padding-left: 2px; white-space: nowrap; }
  .service-column li::before { content: ""; width: 5px; height: 5px; border-radius: 50%; border: 1.5px solid #777; flex: none; }

  .site-footer { position: absolute; left: 0; top: 564px; width: 1200px; height: 30px; background: var(--footer-bg); }
  .copyright { position: absolute; left: 141px; top: 0; line-height: 30px; font-size: 12.5px; color: var(--footer-text); white-space: nowrap; }
  .footer-phone { position: absolute; right: 136px; top: 0; height: 30px; display: flex; align-items: center; gap: 6px; font-family: "Montserrat", sans-serif; font-weight: 500; font-size: 16.5px; color: var(--phone-yellow); white-space: nowrap; }
</style>
</head>
<body>
  <header class="utility-bar">
    <ul class="utility-links">
      <li>Home</li><li>Contact</li><li>Introduction</li>
    </ul>
    <div class="social-dots"><span></span><span></span><span></span></div>
  </header>

  <nav class="main-nav">
    <div class="brand"><span class="brand-mark"></span><span class="brand-name">Vantrel 4</span></div>
    <ul class="nav-links">
      <li>About Us</li><li>Project Control</li><li>Contract Management</li><li>Specialist Services</li><li>Projects</li>
    </ul>
  </nav>

  <section class="hero">
    <h1 class="hero-title">At Vantrel 4 Management Limited</h1>
    <ul class="hero-points">
      <li><svg viewBox="0 0 14 12"><path d="M1 6.5 L5 10 L13 1.5" fill="none" stroke="#5fc43a" stroke-width="2.6"/></svg>Planning &amp; Scheduling</li>
      <li><svg viewBox="0 0 14 12"><path d="M1 6.5 L5 10 L13 1.5" fill="none" stroke="#5fc43a" stroke-width="2.6"/></svg>Cost and Change Control</li>
      <li><svg viewBox="0 0 14 12"><path d="M1 6.5 L5 10 L13 1.5" fill="none" stroke="#5fc43a" stroke-width="2.6"/></svg>Risk Management</li>
      <li><svg viewBox="0 0 14 12"><path d="M1 6.5 L5 10 L13 1.5" fill="none" stroke="#5fc43a" stroke-width="2.6"/></svg>Reporting &amp; Contract Administration</li>
    </ul>
    <div class="hero-visual" role="img" aria-label="Photo of a professional woman touching floating interface panels"></div>
    <div class="cta-button">GET STARTED
      <span class="cta-arrow"><svg width="8" height="10" viewBox="0 0 8 10"><path d="M1 0 L7 5 L1 10 Z" fill="#ffffff"/></svg></span>
    </div>
    <div class="slider-controls">
      <svg width="10" height="14" viewBox="0 0 10 14"><path d="M8 1 L2 7 L8 13" fill="none" stroke="#222" stroke-width="2.4"/></svg>
      <svg width="10" height="14" viewBox="0 0 10 14"><rect x="1" y="1" width="3" height="12" fill="#222"/><rect x="6" y="1" width="3" height="12" fill="#222"/></svg>
      <svg width="10" height="14" viewBox="0 0 10 14"><path d="M2 1 L8 7 L2 13" fill="none" stroke="#222" stroke-width="2.4"/></svg>
    </div>
  </section>
  <div class="hero-base"></div>

  <main class="service-columns">
    <section class="service-column" style="left:140px;width:193px">
      <h2>Project Control</h2>
      <ul><li>Cost Control</li><li>Schedule Control</li><li>Change Control</li><li>Risk &amp; Opportunity Management</li><li>Claim Analysis</li></ul>
    </section>
    <section class="service-column" style="left:398px;width:178px">
      <h2>Contract Management</h2>
      <ul><li>Prime Contract Administration</li><li>Sub Contract Administration</li><li>Sub Contractor Deliverables</li></ul>
    </section>
    <section class="service-column" style="left:661px;width:154px">
      <h2>Specialist Services</h2>
      <ul><li>Engineering Earned Value</li><li>S-Curve Reporting</li><li>Critical Issues Reporting</li><li>Management Schedules</li><li>Six Sigma</li></ul>
    </section>
    <section class="service-column" style="left:911px;width:153px">
      <h2>Recent Projects</h2>
      <ul><li>Rail &amp; Aviation-Projects</li><li>Manufacturing- Projects</li><li>Building</li><li>Infrastructure/Rail- Binds</li></ul>
    </section>
  </main>

  <footer class="site-footer">
    <p class="copyright">Copyright © 2012 Vantrel 4. All Rights Reserved.</p>
    <div class="footer-phone">
      <svg width="20" height="18" viewBox="0 0 20 18"><rect x="2" y="2" width="8" height="14" rx="1.5" fill="none" stroke="#e8e8e8" stroke-width="1.6"/><rect x="4" y="4" width="4" height="5" fill="#e8e8e8"/><path d="M13 5 Q15 9 13 13 M16 3 Q19 9 16 15" fill="none" stroke="#e8e8e8" stroke-width="1.4"/></svg>
      +0987 654 321
    </div>
  </footer>
</body>
</html>
```